VERUNE needs a more polished Packaging Design

VERUNE is a medical device company needing a new look for their packaging design.
• Please refer to File 3 in the attachments to find the template of the current package design.

We want the design to be clean and sophisticated. The logo must not be changed.
• Our Verune logo can be found in File 1 and 2 in the attachments

Industry/Entity Type

It Company

```html
<!DOCTYPE html>
<html lang="en">
<head>
<meta charset="utf-8">
<title>VERUNE Intraocular Lens Packaging Dieline</title>
<link rel="stylesheet" href="https://fonts.googleapis.com/css2?family=Ubuntu:wght@400;500&display=swap">
<style>
  :root {
    --brand-blue: #1d8fd8;
    --ink-blue: #2a6fb0;
    --deep-blue: #1d5d9c;
    --panel: #ffffff;
    --fold: #c9dcea;
    --icon-grey: #555555;
    --backdrop-top: #f4f6f7;
    --backdrop-bottom: #b9c6cc;
    --crystal-light: #e3f2fd;
    --crystal-mid: #a9d6f5;
    --crystal-deep: #5fb3ea;
  }
  * { margin: 0; padding: 0; box-sizing: border-box; }
  html, body { width: 1200px; height: 1000px; overflow: hidden; }
  body {
    background: linear-gradient(180deg, var(--backdrop-top) 0%, var(--backdrop-bottom) 100%);
    font-family: "Ubuntu", sans-serif;
    color: var(--ink-blue);
    position: relative;
  }
  .dieline, .crystal-art { position: absolute; left: 0; top: 0; width: 1200px; height: 1000px; }
  .abs { position: absolute; }

  .brand-name { font-weight: 500; color: var(--brand-blue); letter-spacing: 1px; line-height: 1; white-space: nowrap; }
  .product-line { color: var(--ink-blue); text-transform: uppercase; line-height: 1.15; white-space: nowrap; }
  .product-line strong { font-weight: 500; color: var(--deep-blue); }
  .rule { height: 1px; background: var(--ink-blue); }

  /* lid (printed upside down) */
  .lid-title { left: 220px; top: 30px; width: 200px; transform: rotate(180deg); }
  .lid-title .brand-name { font-size: 30px; margin-top: 6px; }
  .lid-title .product-line { font-size: 13px; }

  /* spine: rotated block kept inside the 60–183 panel */
  .spine-title {
    left: -12px; top: 280px; width: 280px; height: 40px;
    transform: rotate(-90deg); transform-origin: center;
    display: flex; align-items: flex-end; justify-content: space-between;
  }
  .spine-title .brand-name { font-size: 30px; }
  .spine-title .product-block { display: flex; flex-direction: column; }
  .spine-title .product-line { font-size: 11px; }
  .spine-title .rule { margin-top: 3px; }

  /* front */
  .front-title { left: 218px; top: 240px; width: 200px; }
  .front-title .brand-name { font-size: 40px; }
  .front-title .product-line { font-size: 18px; margin-top: 10px; }
  .front-title .rule { margin: 4px 0; width: 196px; }
  .front-spec { left: 218px; top: 400px; width: 142px; font-size: 13px; line-height: 1.45; }
  .front-spec .spec-edge { display: flex; align-items: center; justify-content: flex-end; gap: 4px; }
  .badge-360 { display: inline-flex; align-items: center; justify-content: center; width: 22px; height: 22px; border: 1px solid var(--ink-blue); border-radius: 50%; font-size: 10px; }

  /* side icons */
  .side-icons { left: 708px; top: 160px; display: flex; flex-direction: column; align-items: center; gap: 12px; }
  .side-icons .single-use { font-size: 6px; writing-mode: vertical-rl; line-height: 1.1; color: #444; }

  /* address flap */
  .maker { left: 218px; top: 488px; font-size: 8.6px; line-height: 1.45; color: var(--deep-blue); }
  .maker .maker-name { font-weight: 500; display: flex; align-items: center; gap: 4px; }
  .maker .maker-name::before { content: ""; width: 6px; height: 6px; background: var(--deep-blue); }
  .maker .maker-lines { padding-left: 10px; }
  .maker b { font-weight: 500; }
  .maker .rev { margin-top: 12px; font-size: 7px; padding-left: 10px; }

  /* back */
  .back-title { left: 218px; top: 590px; width: 280px; }
  .back-title .brand-name { font-size: 30px; }
  .back-title .product-line { font-size: 13.5px; margin-top: 8px; }
  .back-title .rule { margin-top: 3px; width: 270px; }
  .info-col { top: 681px; width: 200px; font-size: 7.2px; line-height: 1.3; }
  .info-col p { margin-bottom: 10px; }
  .info-col.left { left: 218px; }
  .info-col.right { left: 388px; }
  .back-icons { left: 218px; top: 833px; display: flex; align-items: center; gap: 20px; }
  .back-icons .single-use { font-size: 7px; line-height: 1.1; color: #444; display: flex; align-items: center; gap: 3px; }
</style>
</head>
<body>

<svg class="dieline" viewBox="0 0 1200 1000" aria-hidden="true">
  <g fill="var(--panel)" stroke="var(--fold)" stroke-width="1">
    <path d="M80,140 L80,60 Q80,48 92,48 L170,48 L183,22 L628,22 L641,48 L645,48 Q655,48 655,60 L655,140 Z"/>
    <path d="M14,140 L746,140 Q760,140 760,154 L760,438 Q760,452 746,452 L14,452 Q0,452 0,438 L0,154 Q0,140 14,140 Z"/>
    <path d="M80,452 L655,452 L655,558 Q655,570 643,570 L92,570 Q80,570 80,558 Z"/>
    <rect x="183" y="570" width="445" height="310"/>
    <path d="M183,880 L628,880 L620,920 L191,920 Z"/>
  </g>
  <g stroke="var(--fold)" stroke-width="1">
    <line x1="60" y1="140" x2="60" y2="452"/>
    <line x1="183" y1="140" x2="183" y2="452"/>
    <line x1="628" y1="140" x2="628" y2="452"/>
    <line x1="700" y1="140" x2="700" y2="452"/>
    <line x1="183" y1="48" x2="183" y2="140"/>
    <line x1="628" y1="48" x2="628" y2="140"/>
    <line x1="183" y1="452" x2="183" y2="570"/>
    <line x1="628" y1="452" x2="628" y2="570"/>
  </g>
</svg>

<svg class="crystal-art" viewBox="0 0 1200 1000" role="img" aria-label="Faceted blue crystal pattern with a concentric eye motif">
  <defs>
    <linearGradient id="crystal" x1="0" y1="0" x2="1" y2="0.3">
      <stop offset="0" stop-color="var(--crystal-light)" stop-opacity="0"/>
      <stop offset="0.35" stop-color="var(--crystal-light)"/>
      <stop offset="0.7" stop-color="var(--crystal-mid)"/>
      <stop offset="1" stop-color="var(--crystal-deep)"/>
    </linearGradient>
  </defs>
  <path d="M395,22 L628,22 L628,570 L470,570 L440,452 L430,300 L410,140 Z" fill="url(#crystal)"/>
</svg>

<div class="abs lid-title">
  <div class="product-line">Hydrophilic Acrylic<br><strong>Intraocular Lens</strong></div>
  <div class="brand-name">VERUNE</div>
</div>

<div class="abs spine-title">
  <div class="brand-name">VERUNE</div>
  <div class="product-block">
    <div class="product-line">Hydrophilic Acrylic</div>
    <div class="product-line"><strong>Intraocular Lens</strong></div>
    <div class="rule"></div>
  </div>
</div>

<div class="abs front-title">
  <div class="brand-name">VERUNE</div>
  <div class="product-line">Hydrophilic Acrylic</div>
  <div class="rule"></div>
  <div class="product-line"><strong>Intraocular Lens</strong></div>
  <div class="rule"></div>
</div>

<div class="abs front-spec">
  <div>Hydrophilic Acrylic</div>
  <div class="spec-edge">Square edge <span class="badge-360">360</span></div>
</div>

<div class="abs side-icons" aria-label="Handling symbols">
  <div class="single-use">Single Use Only</div>
  <svg width="14" height="14" viewBox="0 0 14 14" fill="none" stroke="var(--icon-grey)"><circle cx="7" cy="7" r="5.5"/><path d="M3,3 L11,11 M11,3 L3,11"/></svg>
  <svg width="14" height="14" viewBox="0 0 14 14" fill="none" stroke="var(--icon-grey)"><circle cx="7" cy="7" r="5.5"/><path d="M3,3 L11,11"/></svg>
  <svg width="14" height="14" viewBox="0 0 14 14" fill="none" stroke="var(--icon-grey)"><path d="M7,1.5 L13,12.5 L1,12.5 Z"/><path d="M7,5 L7,9"/></svg>
  <svg width="14" height="22" viewBox="0 0 14 22" fill="none" stroke="var(--icon-grey)"><rect x="1" y="1" width="12" height="20"/><path d="M1,14 L13,14"/></svg>
</div>

<div class="abs maker">
  <div class="maker-name">Northfield Vision Devices Ltd.</div>
  <div class="maker-lines">
    Alder House, Birch Lane, Ashworth, Lancashire<br>
    AB1 2CD, United Kingdom<br>
    Website: <b>www.nfv-devices.com</b> &nbsp; E-mail: <b>info@nfv-devices.com</b>
  </div>
  <div class="rev">REV.06 NVD03062015</div>
</div>

<div class="abs back-title">
  <div class="brand-name">VERUNE</div>
  <div class="product-line">Hydrophilic Acrylic <strong>Intraocular Lens</strong></div>
  <div class="rule"></div>
</div>

<div class="abs info-col left">
  <p>Contains one sterile intraocular lens<br>Do not use if the packaging is damaged<br>Do not resterilize</p>
  <p>Bevat één steriele intraoculaire lens<br>Niet gebruiken als de verpakking beschadigd is<br>Niet opnieuw steriliseren</p>
  <p>Contient une lentille intraoculaire stérile<br>Ne pas utiliser si l'emballage est endommagé<br>Ne pas restériliser</p>
  <p>Enthält eine sterile intraokulare Linse<br>Nicht verwenden, wenn die Verpackung beschädigt<br>ist Nicht resterilisieren</p>
</div>

<div class="abs info-col right">
  <p>Περιέχει ένα αποστειρωμένο ενδοφθάλμιο φακό<br>Μην το χρησιμοποιείτε εάν η συσκευασία έχει υποστεί ζημιά<br>Μην επαναποστειρώνετε</p>
  <p>Contiene una lente intraoculare sterile<br>Non usare se la confezione è danneggiata<br>Non risterilizzare</p>
  <p>Contém uma lente intra-ocular esterilizada<br>Não use se a embalagem está danificada<br>Não reesterilize</p>
  <p>Contiene una lente intraocular estéril<br>No utilizar si el envase está dañado<br>No vuelva a esterilizar</p>
</div>

<div class="abs back-icons" aria-label="Handling symbols">
  <svg width="22" height="14" viewBox="0 0 22 14" fill="none" stroke="var(--icon-grey)"><rect x="1" y="1" width="20" height="12"/><path d="M15,1 L15,13"/></svg>
  <svg width="16" height="14" viewBox="0 0 16 14" fill="none" stroke="var(--icon-grey)"><path d="M8,1 L15,13 L1,13 Z"/><path d="M8,5 L8,9"/></svg>
  <svg width="16" height="16" viewBox="0 0 16 16" fill="none" stroke="var(--icon-grey)"><circle cx="8" cy="8" r="6.5"/><path d="M3.5,3.5 L12.5,12.5"/></svg>
  <svg width="24" height="16" viewBox="0 0 24 16" fill="none" stroke="var(--icon-grey)"><rect x="1" y="3" width="12" height="10"/><circle cx="18" cy="8" r="5"/><path d="M14.5,4.5 L21.5,11.5"/></svg>
  <div class="single-use">
    <svg width="16" height="16" viewBox="0 0 16 16" fill="none" stroke="var(--icon-grey)"><circle cx="8" cy="8" r="6.5"/><path d="M4,4 L12,12 M12,4 L4,12"/></svg>
    <span>Single<br>Use Only</span>
  </div>
</div>

</body>
</html>
```